DOUBLE SIDED BROCHURE NEEDED TO PROMOTE DOCTOR

I need a double sided DL size (99mm x 210mm) brochure, promoting a doctor seeing patients in a new area.

I want something professional. I have included the relevant information. I would also like the Dr's picture somwhere in the brochure, with a professional background. I wish to print these tomorrow, so i will pick a winner within 14 hours of posting this ad.

I have included an example of a brochures design that I recently saw, and its definietly a good starting point.

Industry/Entity Type

Medical

```html
<!DOCTYPE html>
<html lang="en">
<head>
<meta charset="utf-8">
<title>Specialist Surgeon Referral Brochure</title>
<link rel="stylesheet" href="https://fonts.googleapis.com/css2?family=Lato:ital,wght@0,300;0,400;0,700;1,300;1,400&family=Kalam:wght@400&display=swap">
<style>
  :root {
    --stage: #e4e4e4;
    --stage-light: #f7f7f7;
    --panel-blue: #5585c9;
    --panel-blue-soft: #7aa3dc;
    --panel-blue-deep: #2f5fae;
    --panel-blue-pale: #a9c4ea;
    --ink-light: #ffffff;
    --ink-soft: #eaf1fb;
  }
  * { box-sizing: border-box; margin: 0; padding: 0; }
  html, body { width: 1200px; height: 1200px; overflow: hidden; }
  body {
    background: radial-gradient(circle at 50% 45%, var(--stage-light) 0%, var(--stage) 75%);
    font-family: "Lato", Arial, sans-serif;
    color: var(--ink-light);
    position: relative;
  }
  .brochure-side {
    position: absolute;
    top: 210px;
    width: 351px;
    height: 744px;
    background: var(--panel-blue);
    overflow: hidden;
    box-shadow: 0 2px 8px rgba(0,0,0,0.18);
  }
  .side-front { left: 185px; }
  .side-back { left: 654px; }

  /* Front side */
  .team-photo {
    position: absolute; left: 0; top: 0; width: 351px; height: 164px;
    background: linear-gradient(180deg, #e9eef4 0%, #c8d4e4 55%, #7f9fcf 100%);
  }
  .building-photo {
    position: absolute; left: 0; top: 478px; width: 160px; height: 266px;
    background: linear-gradient(90deg, rgba(200,210,225,0.75) 0%, rgba(150,175,210,0.55) 60%, rgba(85,133,201,0) 100%);
  }
  .greeting {
    position: absolute; left: 30px; top: 174px;
    font-family: "Kalam", cursive; font-size: 21px; letter-spacing: 0.5px;
  }
  .announcement {
    position: absolute; left: 30px; top: 218px; width: 290px;
    font-weight: 300; font-size: 20px; line-height: 24px;
  }
  .announcement strong { font-weight: 700; }
  .detail {
    position: absolute; left: 30px; width: 282px;
    font-weight: 400; font-size: 12px; line-height: 17px; color: var(--ink-soft);
  }
  .detail-booking { top: 330px; }
  .detail-skills { top: 418px; }
  .service-list {
    position: absolute; list-style: none; z-index: 2;
    font-size: 12.5px; line-height: 16px; color: var(--ink-soft);
  }
  .service-list li { position: relative; padding-left: 20px; }
  .service-list li::before {
    content: ""; position: absolute; left: 0; top: 4px;
    border-left: 7px solid var(--ink-light);
    border-top: 4px solid transparent; border-bottom: 4px solid transparent;
  }
  .front-services { left: 138px; top: 484px; width: 200px; }
  .front-services li { margin-bottom: 19px; }
  .front-services em { font-style: italic; font-weight: 300; }
  .wave { position: absolute; left: 0; width: 351px; }
  .wave-bottom { bottom: 0; height: 60px; }
  .wave-top { top: 0; height: 70px; }

  /* Back side */
  .corridor-photo {
    position: absolute; inset: 0;
    background: linear-gradient(160deg, #8fb2e3 0%, #6b97d4 40%, #5b8ccf 100%);
  }
  .contact-row { position: absolute; left: 36px; display: flex; gap: 22px; z-index: 2; }
  .contact-row svg { flex: 0 0 auto; margin-top: 6px; }
  .clinic-name { font-weight: 700; font-size: 21px; line-height: 22px; }
  .clinic-address { font-weight: 300; font-size: 20px; line-height: 22px; }
  .contact-text { font-weight: 300; font-size: 20px; line-height: 24px; }
  .contact-text strong { font-weight: 700; }
  .row-address { top: 88px; left: 40px; }
  .row-phone { top: 196px; }
  .row-fax { top: 243px; }
  .general-intro {
    position: absolute; left: 40px; top: 346px; z-index: 2;
    font-weight: 300; font-size: 16px; line-height: 18px;
  }
  .back-services { left: 40px; top: 402px; font-size: 12.5px; line-height: 17.3px; }
  .back-services li { padding-left: 15px; }
  .back-services li::before { top: 4px; border-left-width: 6px; }
  .doctor-photo {
    position: absolute; left: 160px; top: 424px; width: 191px; height: 320px; z-index: 1;
    background: linear-gradient(180deg, rgba(160,126,106,0.85) 0%, #a07e6a 45%, #3b4150 75%, #2e3442 100%);
    border-top-left-radius: 90px;
  }
  .doctor-caption {
    position: absolute; left: 40px; top: 632px; z-index: 2;
    font-style: italic; font-weight: 400; font-size: 14px;
  }
</style>
</head>
<body>

  <section class="brochure-side side-front">
    <div class="team-photo" role="img" aria-label="Photo of a smiling medical team in scrubs and lab coats in a hospital ward"></div>
    <div class="building-photo" role="img" aria-label="Photo of a hospital building entrance with its signage"></div>

    <p class="greeting">Dear Doctors,</p>
    <p class="announcement">We are pleased to announce that <strong>Dr. Karim Haddad</strong> is now consult-ing in Westbay, seeing public and private patients.</p>
    <p class="detail detail-booking">Guaranteed appointment within two weeks, with patients having the option of surgery at Harbourside Health Campus, Ridgeview Hospital or St. Clare's Northgate.</p>
    <p class="detail detail-skills">Dr. Haddad is a highly trained specialised surgeon, in all areas of Endocrine, Breast and General Surgery Including</p>

    <ul class="service-list front-services">
      <li>Thyroid Surgery</li>
      <li>Parathyroid surgery<br><em>(including minimally invasive parathyroidectomy)</em></li>
      <li>Breast Cancer</li>
      <li>Benign breast lesions</li>
    </ul>

    <svg class="wave wave-bottom" viewBox="0 0 351 60" preserveAspectRatio="none" aria-hidden="true">
      <path d="M0 60 L0 52 Q190 46 351 0 L351 60 Z" fill="var(--panel-blue-soft)" opacity="0.6"/>
      <path d="M0 60 L0 56 Q200 52 351 14 L351 60 Z" fill="var(--panel-blue-deep)"/>
    </svg>
  </section>

  <section class="brochure-side side-back">
    <div class="corridor-photo" role="img" aria-label="Faint photo of a bright hospital corridor as background"></div>

    <svg class="wave wave-top" viewBox="0 0 351 70" preserveAspectRatio="none" aria-hidden="true">
      <path d="M0 0 L351 0 L351 14 Q120 18 0 70 Z" fill="var(--panel-blue-pale)" opacity="0.7"/>
      <path d="M0 0 L351 0 L351 6 Q110 10 0 56 Z" fill="var(--panel-blue-deep)"/>
    </svg>

    <div class="contact-row row-address">
      <svg width="12" height="18" viewBox="0 0 12 18" aria-hidden="true" style="margin-top:26px">
        <path d="M6 0 C2.7 0 0 2.6 0 5.9 C0 10 6 18 6 18 C6 18 12 10 12 5.9 C12 2.6 9.3 0 6 0 Z M6 8.3 A2.4 2.4 0 1 1 6 3.5 A2.4 2.4 0 0 1 6 8.3 Z" fill="var(--ink-light)"/>
      </svg>
      <div>
        <p class="clinic-name">Westbay Clinic:</p>
        <p class="clinic-address">42 Coralwood Road<br>Westbay WA 6310.</p>
      </div>
    </div>

    <div class="contact-row row-phone">
      <svg width="17" height="17" viewBox="0 0 24 24" aria-hidden="true" style="margin-top:3px">
        <path d="M6.6 10.8 C8 13.6 10.4 16 13.2 17.4 L15.4 15.2 C15.7 14.9 16.1 14.8 16.4 15 C17.5 15.4 18.7 15.6 20 15.6 C20.6 15.6 21 16 21 16.6 L21 20 C21 20.6 20.6 21 20 21 C10.6 21 3 13.4 3 4 C3 3.4 3.4 3 4 3 L7.5 3 C8.1 3 8.5 3.4 8.5 4 C8.5 5.3 8.7 6.5 9.1 7.6 C9.2 7.9 9.1 8.3 8.9 8.6 Z" fill="var(--ink-light)"/>
      </svg>
      <p class="contact-text">Phone: <strong>1300 482 117</strong></p>
    </div>

    <div class="contact-row row-fax">
      <svg width="20" height="20" viewBox="0 0 20 20" aria-hidden="true">
        <rect x="0" y="5" width="5" height="14" rx="1" fill="var(--ink-light)"/>
        <rect x="6" y="5" width="14" height="14" rx="1" fill="var(--ink-light)"/>
        <rect x="9" y="1" width="9" height="6" fill="var(--ink-light)"/>
        <g fill="var(--panel-blue)">
          <rect x="9" y="10" width="2" height="2"/><rect x="12" y="10" width="2" height="2"/><rect x="15" y="10" width="2" height="2"/>
          <rect x="9" y="14" width="2" height="2"/><rect x="12" y="14" width="2" height="2"/><rect x="15" y="14" width="2" height="2"/>
        </g>
      </svg>
      <p class="contact-text">Please send all referrals<br>by fax to <strong>(08) 6421 3058</strong>.</p>
    </div>

    <p class="general-intro">All areas of general surgery,<br>such as</p>
    <ul class="service-list back-services">
      <li>Gallbladder surgery</li>
      <li>Hernia surgery</li>
      <li>Haemorrhoids</li>
      <li>Carpal Tunnel</li>
      <li>Vasectomy</li>
    </ul>

    <div class="doctor-photo" role="img" aria-label="Portrait photo of the surgeon in glasses, a dark jacket and checked shirt"></div>
    <p class="doctor-caption">Dr. Karim Haddad</p>
  </section>

</body>
</html>
```